Business IT Services Billboard to attract local small businesses

We are Brivolane, a premier Managed Service Provider (MSP) specializing in comprehensive IT services and VOIP phone solutions exclusively for businesses. Our goal is to create a dynamic and visually engaging billboard advertisement that not only highlights our cutting-edge IT solutions but also emphasizes our state-of-the-art VOIP phone services. This billboard should communicate our commitment to providing innovative, reliable, and holistic technology solutions.
Target Market(s)
small business
Industry/Entity Type
Information Technology
Colors
Designer to choose colors to be used in the design.
Look and feel
Each slider illustrates characteristics of the customer's brand and the style your logo design should communicate.

```html
<!DOCTYPE html>
<html lang="en">
<head>
<meta charset="UTF-8">
<title>Brivolane Billboard</title>
<link href="https://fonts.googleapis.com/css2?family=Exo+2:wght@300;400;500;600;700;800&display=swap" rel="stylesheet">
<style>
  :root {
    --blue: #1b6fc2;
    --dark: #3b3c3f;
    --ink: #37383b;
    --white: #ffffff;
    --stage: #7a7a7a;
    --light-a: #f7f9fb;
    --light-b: #e4eaef;
  }
  * { margin: 0; padding: 0; box-sizing: border-box; }
  html, body { width: 1200px; height: 703px; overflow: hidden; }
  body {
    background: var(--stage);
    font-family: "Exo 2", sans-serif;
    position: relative;
  }
  .billboard {
    position: absolute;
    left: 20px; top: 61px;
    width: 1194px; height: 598px;
    transform: scale(0.9715);
    transform-origin: 0 0;
    background: linear-gradient(100deg, var(--light-a) 0%, #ffffff 35%, var(--light-b) 100%);
    overflow: hidden;
  }
  .billboard svg.shapes { position: absolute; left: 0; top: 0; }
  .photo-area {
    position: absolute;
    left: 600px; top: 110px;
    width: 594px; height: 370px;
    background: radial-gradient(ellipse at 60% 55%, #3a3f4a 0%, #6b7480 30%, #cfd6dd 60%, #edf1f4 100%);
  }
  .brand {
    position: absolute; left: 55px; top: 38px;
    font-size: 74px; font-weight: 800; letter-spacing: 3px;
    color: var(--blue); line-height: 1;
  }
  .phone {
    position: absolute; left: 828px; top: 42px;
    font-size: 44px; font-weight: 700; color: var(--white); line-height: 1;
  }
  .headline { position: absolute; left: 55px; top: 140px; color: var(--ink); line-height: 1; }
  .headline .elevate { font-size: 64px; font-weight: 800; display: block; }
  .headline .band { display: flex; margin-top: 14px; height: 60px; }
  .headline .band .fill {
    background: var(--blue); color: var(--white);
    font-size: 40px; font-weight: 700; padding: 8px 18px 0 20px;
  }
  .headline .band .outline {
    border: 2px solid var(--blue); color: var(--blue);
    font-size: 40px; font-weight: 500; padding: 6px 12px 0 12px; background: var(--white);
  }
  .headline .line { display: block; font-size: 64px; margin-top: 10px; }
  .headline .bold { font-weight: 800; }
  .headline .regular { font-weight: 400; }
  .headline .accent { color: var(--blue); }
  .tagline {
    position: absolute; left: 55px; top: 488px;
    font-size: 25px; font-weight: 600; color: var(--white); line-height: 1.35;
  }
  .cta {
    position: absolute; right: 44px; top: 494px; text-align: right;
    color: var(--white); font-size: 28px; line-height: 1.2;
  }
  .cta .lead { font-weight: 400; display: block; }
  .cta .url { font-weight: 700; display: block; }
</style>
</head>
<body>
  <div class="billboard">
    <div class="photo-area" role="img" aria-label="Photo of a smiling support agent wearing a headset, working at a laptop in a bright office"></div>
    <svg class="shapes" width="1194" height="598" viewBox="0 0 1194 598">
      <rect x="0" y="0" width="1194" height="12" fill="var(--dark)"/>
      <path d="M722 0 H1194 V110 H805 Q795 110 790 102 L745 22 Q738 12 722 12 Z" fill="var(--dark)"/>
      <path d="M722 12 Q738 12 745 22 L752 35" fill="none" stroke="var(--blue)" stroke-width="5"/>
      <path d="M0 457 H628 Q645 457 655 470 L735 590 H1194 V598 H0 Z" fill="var(--dark)"/>
      <path d="M668 480 H1194 V585 H752 Q742 585 735 575 Z" fill="var(--blue)"/>
      <circle cx="780" cy="72" r="30" fill="var(--blue)" stroke="var(--white)" stroke-width="4"/>
      <path d="M769 60 l6 -2 4 9 -4 3 q3 8 10 12 l3 -4 9 4 -2 6 q-2 3 -6 3 q-14 -2 -22 -20 q0 -8 2 -11 Z" fill="none" stroke="var(--white)" stroke-width="2.5" stroke-linejoin="round"/>
      <path d="M785 58 q9 1 11 11 M785 51 q15 2 17 17" fill="none" stroke="var(--white)" stroke-width="2.2" stroke-linecap="round"/>
    </svg>
    <div class="brand">BRIVOLANE</div>
    <div class="phone">(555) 410-2287</div>
    <div class="headline">
      <span class="elevate">ELEVATE</span>
      <div class="band"><span class="fill">YOUR BUSINESS</span><span class="outline">with</span></div>
      <span class="line"><span class="bold">Next-Gen IT</span> <span class="regular">and</span></span>
      <span class="line"><span class="bold accent">VOIP</span> <span class="bold">Services</span></span>
    </div>
    <p class="tagline">Innovative IT and VOIP Solutions Tailored<br>for Your Business Success.</p>
    <p class="cta"><span class="lead">Transform Your Tech Today at</span><span class="url">www.Brivolane.com</span></p>
  </div>
</body>
</html>
```